ultra-minimalist business card

front (black background, matte):

tarik b. hosseny
writer | photographer
get@tarikhosseny.com

back (white background, matte):

a picture speaks a thousand words;
a word draws a thousand pictures.

www.tarikhosseny.com

all text should be small (white or silver - as long as it shows against the black - on the front; black or gray - as long as it shows against the white - on the back).

feel free to get creative in terms of arrangement, alignment, and font type, but remember, the overall style is minimalist, so nothing too fancy, please.

thanks.

```html
<!DOCTYPE html>
<html lang="en">
<head>
<meta charset="utf-8">
<title>Tarik B. Hosseny – Business Card</title>
<link rel="stylesheet" href="https://fonts.googleapis.com/css2?family=Libre+Baskerville:wght@400;700&family=Montserrat:wght@400;500&display=swap">
<style>
  :root {
    --backdrop: #161617;
    --card-black: #1d1d1f;
    --card-grey: #4b4b4d;
    --panel-dark: #1f2022;
    --silver-light: #e6e6e8;
    --silver-mid: #a9a9ad;
    --silver-dark: #6f6f74;
    --text-soft: #d8d8da;
    --text-muted: #9c9ca0;
  }
  * { margin: 0; padding: 0; box-sizing: border-box; }
  html, body {
    width: 1200px;
    height: 1000px;
    overflow: hidden;
    background: var(--backdrop);
  }
  .canvas {
    width: 1200px;
    height: 1000px;
    display: flex;
    flex-direction: column;
    align-items: center;
    justify-content: center;
    gap: 60px;
  }
  .card {
    position: relative;
    width: 640px;
    height: 366px;
    border-radius: 28px;
    overflow: hidden;
    box-shadow: 0 18px 40px rgba(0, 0, 0, 0.55);
  }

  /* Front side: name only */
  .card--front {
    background: var(--card-black);
    display: flex;
    align-items: center;
    justify-content: center;
  }
  .front-name {
    font-family: "Libre Baskerville", serif;
    font-weight: 400;
    font-size: 34px;
    letter-spacing: 1px;
    text-transform: uppercase;
    background: linear-gradient(180deg, var(--silver-light) 0%, var(--silver-mid) 50%, var(--silver-dark) 100%);
    -webkit-background-clip: text;
    background-clip: text;
    color: transparent;
  }

  /* Back side: contact panel and motto */
  .card--back {
    background: var(--card-grey);
  }
  .contact-panel {
    position: absolute;
    left: 0;
    top: 104px;
    width: 418px;
    height: 178px;
    background: var(--panel-dark);
    border-radius: 0 30px 30px 0;
    padding: 38px 0 0 34px;
  }
  .contact-name {
    font-family: "Libre Baskerville", serif;
    font-size: 23px;
    line-height: 1;
    color: var(--silver-mid);
  }
  .contact-name strong {
    font-weight: 700;
    color: var(--silver-light);
  }
  .contact-role {
    margin-top: 8px;
    font-family: "Montserrat", sans-serif;
    font-size: 15px;
    color: var(--text-muted);
    letter-spacing: 0.3px;
  }
  .contact-list {
    list-style: none;
    margin-top: 8px;
    font-family: "Montserrat", sans-serif;
    font-size: 15px;
    line-height: 1.5;
    color: var(--text-soft);
  }
  .contact-list .label {
    display: inline-block;
    width: 26px;
    font-weight: 500;
    color: var(--silver-mid);
  }
  .motto {
    position: absolute;
    right: 30px;
    bottom: 28px;
    font-family: "Montserrat", sans-serif;
    font-size: 13px;
    color: var(--text-soft);
    letter-spacing: 0.2px;
  }
</style>
</head>
<body>
  <main class="canvas">
    <section class="card card--front" aria-label="Card front">
      <h1 class="front-name">Tarik B. Hosseny</h1>
    </section>

    <section class="card card--back" aria-label="Card back">
      <div class="contact-panel">
        <p class="contact-name">tarik b. <strong>hosseny</strong></p>
        <p class="contact-role">writer | photographer</p>
        <ul class="contact-list">
          <li><span class="label">E:</span>get@tarikhosseny.com</li>
          <li><span class="label">W:</span>www.tarikhosseny.com</li>
        </ul>
      </div>
      <p class="motto">a picture speaks a thousand words; - a word draws a thousand pictures.</p>
    </section>
  </main>
</body>
</html>
```